Website for a new t-shirt company called brightroamapperal.com

We are looking for a talented web designer to create a website that aligns with our brand's message and identity centered around the theme of "Bright Roam." The website should be modern, clean, and visually appealing while also being user-friendly and easy to navigate.

We will be using the Big Commerce platform for our online store section, so the designer should have experience in designing websites on this platform.

We would like the website to have the following elements:

A color scheme that aligns with the brand's identity and message
A homepage that showcases our products and message, with clear calls-to-action for visitors to explore further
A blog section that highlights our brand's philosophy and offers advice and tips for people looking to make positive changes in their lives
An "About Us" section that introduces our brand and team and offers insight into our mission and values
A contact form that allows visitors to easily get in touch with us for inquiries or support
We are open to creative suggestions and ideas from the designer, but we would like the website to have a modern and minimalist aesthetic that resonates with our target audience of 20 to 40-year-olds.

```html
<!DOCTYPE html>
<html lang="en">
<head>
<meta charset="utf-8">
<title>Bright Roam</title>
<link href="https://fonts.googleapis.com/css2?family=Open+Sans:wght@400;600;700;800&display=swap" rel="stylesheet">
<style>
:root{
  --lime:#bcff00;
  --black:#000;
  --ink:#222;
  --text:#444;
  --muted:#666;
  --footer:#1f1f1f;
  --footer-bottom:#151515;
  --card:#f2f2f2;
  --star:#f2c21b;
  --white:#fff;
}
*{box-sizing:border-box;margin:0;padding:0}
html,body{width:1200px;height:3237px;overflow:hidden}
body{position:relative;font-family:'Open Sans',sans-serif;color:var(--ink);background:var(--white)}
.abs{position:absolute}

/* top bar */
.topbar{top:0;left:0;width:1200px;height:39px;background:var(--white);font-size:12px;color:var(--ink)}
.topbar .notice{left:0;width:1200px;top:11px;text-align:center}
.topbar .cart{left:808px;top:10px;display:flex;align-items:center;gap:8px}
.topbar .badge{left:924px;top:5px;width:28px;height:28px;border-radius:50%;background:var(--lime);font-size:12px;text-align:center;line-height:28px}
.topbar .account{left:986px;top:11px}

/* nav */
.nav{top:39px;left:0;width:1200px;height:83px;background:var(--black);color:var(--white)}
.brand{left:112px;top:24px;font-size:30px;font-weight:600;color:var(--white);letter-spacing:.5px;white-space:nowrap}
.nav .links{left:476px;top:30px;font-size:16px}
.nav .links span{position:absolute;white-space:nowrap}
.search{left:926px;top:23px;width:162px;height:39px;border:1px solid #777;display:flex;align-items:center;gap:8px;padding-left:16px;font-size:14px;color:#ccc}

/* sale band */
.sale{top:122px;left:0;width:1200px;height:45px;background:var(--lime);text-align:center;font-size:14px;font-weight:600;line-height:45px;color:var(--ink)}

/* hero */
.hero{top:167px;left:0;width:1200px;height:386px;background:linear-gradient(90deg,#7a6a5c 0%,#b9aea2 18%,#8e8782 34%,#4e4c4f 55%,#3b3c42 75%,#2f3035 100%)}
.hero .welcome{left:755px;top:92px;font-size:28px;font-weight:600;color:#eee;letter-spacing:.5px;white-space:nowrap}
.hero .title{left:755px;top:134px;font-size:52px;font-weight:800;color:#eee;letter-spacing:1px;line-height:1.2;white-space:nowrap}
.btn-lime{background:var(--lime);color:var(--ink);font-weight:700;text-align:center}
.hero .cta{left:755px;top:225px;width:133px;height:46px;line-height:46px;font-size:16px}
.hero .dot{top:344px;width:10px;height:10px;border-radius:50%;border:1.5px solid #fff}
.hero .dot.on{background:#fff}

/* section headings */
.section-title{left:0;width:1200px;text-align:center;font-size:40px;font-weight:700;color:var(--ink);letter-spacing:.5px}

/* category tiles */
.tile{overflow:hidden}
.tile .label{position:absolute;left:28px;color:var(--white)}
.tile h3{font-size:21px;font-weight:700}
.tile p{font-size:14px;margin-top:12px;white-space:nowrap}
.tile .shop{margin-top:22px;width:133px;height:45px;background:var(--white);color:var(--ink);font-weight:700;font-size:15px;text-align:center;line-height:45px}
.tile-men{left:112px;top:700px;width:474px;height:268px;background:linear-gradient(180deg,#cfcac4 0%,#8c7a62 55%,#3c3a38 100%)}
.tile-kids{left:112px;top:984px;width:474px;height:267px;background:linear-gradient(180deg,#a7b69a 0%,#6f6b5f 45%,#2c2b2a 100%)}
.tile-women{left:604px;top:700px;width:484px;height:551px;background:linear-gradient(180deg,#5d6a73 0%,#b9b6b1 40%,#9a8f86 70%,#4a4f5a 100%)}

/* product cards */
.product{width:210px}
.product .img{height:257px;background:var(--card)}
.product .desc{margin-top:21px;font-size:14px;line-height:20px;color:var(--muted)}
.product .stars{margin-top:6px;font-size:24px;color:var(--star);letter-spacing:-1px;line-height:30px}
.product .price{margin-top:4px;font-size:17px;color:var(--ink)}
.product .swatches{margin-top:8px;display:flex;gap:12px}
.product .swatches i{width:13px;height:13px;border-radius:50%;display:block}

.divider{left:112px;top:1769px;width:976px;height:1px;background:#ccc}

/* about */
.about-copy{left:130px;top:1908px;width:940px;text-align:center;font-size:16px;line-height:30px;color:var(--text)}
.value{width:260px;text-align:center}
.value svg{display:block;margin:0 auto}
.value h4{margin-top:10px;font-size:14px;font-weight:600;color:var(--ink)}
.value p{font-size:14px;line-height:22px;color:var(--text);margin-top:4px}

/* blog */
.post{top:2381px;width:228px;height:382px;color:var(--white);text-align:center}
.post .inner{position:absolute;left:0;right:0;top:212px}
.post h3{font-size:17px;font-weight:700}
.post .rule{width:46px;height:3px;background:var(--lime);margin:8px auto 0}
.post p{margin-top:20px;font-size:15px;line-height:28px;padding:0 8px}

/* footer */
.footer{top:2847px;left:0;width:1200px;height:390px;background:var(--footer);color:var(--white)}
.contact-title{left:114px;top:44px;font-size:26px;font-weight:800;white-space:nowrap}
.field{top:43px;height:47px;background:var(--white);color:#888;font-size:14px;padding-left:16px;line-height:47px}
.submit{left:954px;top:43px;width:101px;height:47px;line-height:47px;font-size:15px}
.footer .brand{top:140px;font-size:32px}
.fcol{top:130px;font-size:14px;line-height:28.3px;text-transform:uppercase;white-space:nowrap}
.fcol b{font-weight:600}
.social{left:922px;top:276px;display:flex;gap:21px}
.social i{width:18px;height:18px;border-radius:50%;background:var(--white);display:block}
.bottom{left:0;top:348px;width:1200px;height:42px;background:var(--footer-bottom)}
.bottom .copy{left:113px;top:12px;font-size:14px}
.payments{left:852px;top:13px;display:flex;gap:9px}
.payments i{width:26px;height:17px;border-radius:2px;display:block}
</style>
</head>
<body>

<header>
  <div class="abs topbar">
    <div class="abs notice">COVID-19 SHIPPING DELAY NOTICE</div>
    <div class="abs cart">
      <svg width="14" height="16" viewBox="0 0 14 16" fill="none" stroke="#222" stroke-width="1.5"><rect x="1.5" y="5" width="11" height="10"/><path d="M4.5 5V3.5a2.5 2.5 0 0 1 5 0V5"/></svg>
      <span>Shopping Cart</span>
    </div>
    <div class="abs badge">0</div>
    <div class="abs account">Sign In or Register</div>
  </div>

  <nav class="abs nav">
    <div class="abs brand">Bright Roam</div>
    <div class="abs links">
      <span style="left:0">Home</span>
      <span style="left:84px">About</span>
      <span style="left:167px">Products</span>
      <span style="left:272px">Blog</span>
      <span style="left:343px">Contact</span>
    </div>
    <div class="abs search">
      <svg width="16" height="16" viewBox="0 0 16 16" fill="none" stroke="#ddd" stroke-width="1.6"><circle cx="6.5" cy="6.5" r="5"/><path d="M10.5 10.5L15 15"/></svg>
      <span>Search</span>
    </div>
  </nav>

  <div class="abs sale">SALE UP TO 70% OFF ON SELECTED ITEMS*</div>
</header>

<section class="abs hero" role="img" aria-label="Photo of a man in sunglasses wearing a white Bright Roam t-shirt on a city street">
  <div class="abs welcome">WELCOME TO</div>
  <div class="abs title">BRIGHT ROAM</div>
  <div class="abs btn-lime cta">SHOP NOW</div>
  <span class="abs dot on" style="left:586px"></span>
  <span class="abs dot" style="left:603px"></span>
</section>

<h2 class="abs section-title" style="top:602px">OUR PRODUCTS</h2>

<section>
  <div class="abs tile tile-men" role="img" aria-label="Photo of a young man in a mustard t-shirt sitting on steps">
    <div class="label" style="top:114px">
      <h3>MEN TSHIRT</h3>
      <p>Lorem ipsum dolor sit amet, consectetur adipiscing elit,</p>
      <div class="shop">SHOP NOW</div>
    </div>
  </div>
  <div class="abs tile tile-kids" role="img" aria-label="Photo of a boy in a black t-shirt holding a skateboard at a skatepark">
    <div class="label" style="top:114px">
      <h3>KIDS TSHIRT</h3>
      <p>Lorem ipsum dolor sit amet, consectetur adipiscing elit,</p>
      <div class="shop">SHOP NOW</div>
    </div>
  </div>
  <div class="abs tile tile-women" role="img" aria-label="Photo of two women in white t-shirts, caps and sunglasses">
    <div class="label" style="top:398px;left:38px">
      <h3>WOMEN TSHIRT</h3>
      <p>Lorem ipsum dolor sit amet, consectetur adipiscing elit,</p>
      <div class="shop">SHOP NOW</div>
    </div>
  </div>
</section>

<section>
  <div class="abs product" style="left:112px;top:1283px">
    <div class="img" role="img" aria-label="Grey t-shirt product shot" style="background:radial-gradient(circle at 50% 48%,#9a9a9a 0 28%,var(--card) 29%)"></div>
    <p class="desc">Lorem ipsum dolr sit amet, consectetur adipiscing.</p>
    <div class="stars">★★★★★</div>
    <div class="price">$427</div>
    <div class="swatches"><i style="background:var(--lime)"></i><i style="background:#222"></i></div>
  </div>
  <div class="abs product" style="left:368px;top:1283px">
    <div class="img" role="img" aria-label="Black t-shirt product shot" style="background:radial-gradient(circle at 50% 48%,#111 0 28%,var(--card) 29%)"></div>
    <p class="desc">Lorem ipsum dolr sit amet, consectetur adipiscing.</p>
    <div class="stars">★★★★★</div>
    <div class="price">$427</div>
    <div class="swatches"><i style="background:var(--lime)"></i><i style="background:#222"></i></div>
  </div>
  <div class="abs product" style="left:624px;top:1283px">
    <div class="img" role="img" aria-label="Lime green t-shirt product shot" style="background:radial-gradient(circle at 50% 48%,#a6f21c 0 28%,var(--card) 29%)"></div>
    <p class="desc">Lorem ipsum dolr sit amet, consectetur adipiscing.</p>
    <div class="stars">★★★★★</div>
    <div class="price">$427</div>
    <div class="swatches"><i style="background:var(--lime)"></i><i style="background:#222"></i></div>
  </div>
  <div class="abs product" style="left:880px;top:1283px">
    <div class="img" role="img" aria-label="Oatmeal t-shirt product shot" style="background:radial-gradient(circle at 50% 48%,#cfc6b8 0 28%,var(--card) 29%)"></div>
    <p class="desc">Lorem ipsum dolr sit amet, consectetur adipiscing.</p>
    <div class="stars">★★★★★</div>
    <div class="price">$427</div>
    <div class="swatches"><i style="background:var(--lime)"></i><i style="background:#222"></i></div>
  </div>
</section>

<div class="abs divider"></div>

<section>
  <h2 class="abs section-title" style="top:1819px">ABOUT US</h2>
  <p class="abs about-copy">Lorem ipsum dolor sit amet, consectetur adipiscing elit, sed do eiusmod tempor incididunt ut labore et dolore magna aliqua. Ut enim ad minim veniam, quis nostrud exercitation ullamco laboris nisi ut aliquip ex ea commodo consequat. Duis aute irure dolor in reprehenderit in voluptate velit esse cillum dolore eu fugiat nulla pariatur. Excepteur sint occaecat cupidatat non proident, sunt in culpa qui officia deserunt mollit anim id est laborum.</p>

  <div class="abs value" style="left:178px;top:2070px">
    <svg width="50" height="50" viewBox="0 0 50 50" fill="none" stroke="#222" stroke-width="2"><circle cx="23" cy="27" r="20"/><circle cx="23" cy="27" r="13"/><circle cx="23" cy="27" r="6"/><path d="M23 27L40 10M36 6v8h8"/></svg>
    <h4>MISSION</h4>
    <p>Duis aute irure dolor in reprehenderit<br>in voluptate velit esse cillum</p>
  </div>
  <div class="abs value" style="left:469px;top:2070px">
    <svg width="56" height="50" viewBox="0 0 56 50" fill="none" stroke="#222" stroke-width="2"><path d="M16 18h24l8 9-20 21-20-21z M8 27h40 M22 27l6 21 6-21 M16 18l6 9 6-9 6 9 6-9"/><path d="M28 2v7 M14 6l4 5 M42 6l-4 5"/></svg>
    <h4>VALUES</h4>
    <p>Duis aute irure dolor in reprehenderit<br>in voluptate velit esse cillum</p>
  </div>
  <div class="abs value" style="left:761px;top:2070px">
    <svg width="62" height="50" viewBox="0 0 62 50" fill="none" stroke="#222" stroke-width="2"><circle cx="31" cy="16" r="8"/><circle cx="15" cy="20" r="6"/><circle cx="47" cy="20" r="6"/><path d="M17 44c0-10 6-16 14-16s14 6 14 16z M4 42c0-8 5-13 11-13 M58 42c0-8-5-13-11-13"/></svg>
    <h4>TEAM</h4>
    <p>Duis aute irure dolor in reprehenderit<br>in voluptate velit esse cillum</p>
  </div>
</section>

<section>
  <h2 class="abs section-title" style="top:2282px;left:5px">OUR BLOG</h2>
  <article class="abs post" style="left:112px;background:linear-gradient(180deg,#d9d4cc 0%,#b49560 45%,#6b4f22 75%,#3a2c16 100%)" role="img" aria-label="Photo of a young man in a mustard t-shirt shading his eyes">
    <div class="inner"><h3>Lorem Ipsum</h3><div class="rule"></div><p>Lorem ipsum dolor sit amet, consectetur adipisc ing elit, sed do eismod.</p></div>
  </article>
  <article class="abs post" style="left:361px;background:linear-gradient(180deg,#e3e0da 0%,#7d7a76 40%,#2a2a2a 75%,#151515 100%)" role="img" aria-label="Photo of a woman in a beanie and sunglasses wearing a black t-shirt">
    <div class="inner"><h3>Lorem Ipsum</h3><div class="rule"></div><p>Lorem ipsum dolor sit amet, consectetur adipisc ing elit, sed do eismod.</p></div>
  </article>
  <article class="abs post" style="left:611px;background:linear-gradient(180deg,#e4e4e2 0%,#a8a8a6 40%,#3a3a3a 75%,#1c1c1c 100%)" role="img" aria-label="Photo of a bearded man in a cap and black t-shirt">
    <div class="inner"><h3>Lorem Ipsum</h3><div class="rule"></div><p>Lorem ipsum dolor sit amet, consectetur adipisc ing elit, sed do eismod.</p></div>
  </article>
  <article class="abs post" style="left:859px;background:linear-gradient(180deg,#a8c6d6 0%,#d8b2c8 45%,#9a7a5a 75%,#4a3a22 100%)" role="img" aria-label="Photo of a smiling woman in a tie-dye t-shirt dancing">
    <div class="inner"><h3>Lorem Ipsum</h3><div class="rule"></div><p>Lorem ipsum dolor sit amet, consectetur adipisc ing elit, sed do eismod.</p></div>
  </article>
</section>

<footer class="abs footer">
  <h2 class="abs contact-title">GET IN TOUCH FORM</h2>
  <div class="abs field" style="left:413px;width:263px">Name</div>
  <div class="abs field" style="left:684px;width:262px">Email</div>
  <div class="abs btn-lime submit">SUBMIT</div>

  <div class="abs brand" style="left:112px">Bright Roam</div>

  <div class="abs fcol" style="left:336px"><b>Shop</b><br>New In<br>Women<br>Men<br>Shoes<br>Accessories<br>Shop Outlet</div>
  <div class="abs fcol" style="left:499px"><b>Further Info</b><br>About Us<br>Contact Us<br>Shipping &amp; Returns<br>Privacy Policy<br>Blog<br>Gift Certificates</div>
  <div class="abs fcol" style="left:713px"><b>Popular Brands</b><br>Arlo Design<br>Bellawear<br>Ona Vale<br>Mira Dress<br>Someday<br>View All</div>
  <div class="abs fcol" style="left:908px"><b>Info</b><br>412 Harbor Lane<br>Bayview, CA 90210<br>Call us at (555)-010-4821</div>

  <div class="abs social" aria-label="Social links"><i></i><i></i><i></i><i></i><i></i></div>

  <div class="abs bottom">
    <div class="abs copy">© Bright Roam. All Rights Reserved.</div>
    <div class="abs payments" aria-label="Accepted payment methods">
      <i style="background:#2a3d8f"></i><i style="background:#d8d8d8"></i><i style="background:#5f8fc9"></i><i style="background:#e9e9e9"></i><i style="background:#3b62b0"></i><i style="background:#f1f1f1"></i><i style="background:#f4c81e"></i>
    </div>
  </div>
</footer>

</body>
</html>
```